BSC Flyer to attract applicants 11x17

Brightline Stagecraft Company provides crew for local concerts, filming, theater, and corporate events.
The flyer will be posted on bulletin boards at colleges with theater programs.
Our primary venues are historic theaters in downtown LA
Need a 11x17 poster to attract potential applicants/crew
I have attached a poster that one of our staff made that has all if the relevant info - but i know the poster can look much better than that. I have also attached many images and our logo. It is not necessary to use all of the images, or any of them. The two images of the theater interiors are the venues we operate so they would be the first to include. I can send additional info or images upon request. Thank you

Entertainment

• APPLY@BSCCREWHUB.LA

```html
<!DOCTYPE html>
<html lang="en">
<head>
<meta charset="UTF-8">
<title>Brightline Stagecraft Company – Open Positions</title>
<link rel="stylesheet" href="https://fonts.googleapis.com/css2?family=Poppins:wght@400;600;700&display=swap">
<style>
  :root {
    --navy: #13233f;
    --brand-blue: #1d4fa0;
    --white: #ffffff;
    --city-top: #0f1c46;
    --city-mid: #2a3d7a;
    --city-bottom: #3b2f3a;
    --stage-light: #dfe4ff;
    --stage-mid: #4b4fa8;
    --stage-dark: #07081a;
    --hall-top: #5a2a78;
    --hall-mid: #8a3348;
    --hall-bottom: #2c1a4a;
    --gold-light: #e0a050;
    --gold-mid: #a5561f;
    --gold-dark: #4a1a12;
  }
  * { margin: 0; padding: 0; box-sizing: border-box; }
  html, body { width: 812px; height: 1200px; overflow: hidden; background: var(--white); }
  .poster {
    position: relative;
    width: 812px;
    height: 1200px;
    font-family: "Poppins", sans-serif;
    color: var(--white);
    background: var(--white);
    overflow: hidden;
  }
  .poster-art { position: absolute; inset: 0; }
  .brand {
    position: absolute;
    top: 40px;
    left: 146px;
    display: flex;
    align-items: center;
    gap: 20px;
  }
  .brand-dot {
    width: 120px;
    height: 120px;
    border-radius: 50%;
    background: var(--brand-blue);
  }
  .brand-name {
    color: var(--brand-blue);
    font-weight: 600;
    line-height: 1.1;
  }
  .brand-name .line-main { display: block; font-size: 30px; letter-spacing: 0.3px; }
  .brand-name .line-sub { display: block; font-size: 18px; letter-spacing: 15px; margin-top: 6px; }
  .content {
    position: absolute;
    left: 0;
    right: 0;
    top: 886px;
    text-align: center;
  }
  .headline {
    font-size: 62px;
    font-weight: 400;
    line-height: 1.1;
    letter-spacing: 0.5px;
  }
  .intro {
    margin-top: 20px;
    font-size: 15px;
    line-height: 1.3;
  }
  .apply-label {
    margin-top: 32px;
    font-size: 16px;
  }
  .apply-email {
    display: inline-block;
    margin-top: 8px;
    width: 319px;
    height: 38px;
    line-height: 38px;
    border-radius: 19px;
    background: var(--white);
    color: var(--brand-blue);
    font-weight: 700;
    font-size: 20px;
  }
  .services {
    margin-top: 36px;
    font-size: 16.5px;
  }
</style>
</head>
<body>
<main class="poster">
  <svg class="poster-art" width="812" height="1200" viewBox="0 0 812 1200">
    <defs>
      <linearGradient id="city-tone" x1="0" y1="0" x2="0" y2="1">
        <stop offset="0" stop-color="var(--city-top)"/>
        <stop offset="0.6" stop-color="var(--city-mid)"/>
        <stop offset="1" stop-color="var(--city-bottom)"/>
      </linearGradient>
      <radialGradient id="stage-tone" cx="0.45" cy="0.35" r="0.65">
        <stop offset="0" stop-color="var(--stage-light)"/>
        <stop offset="0.35" stop-color="var(--stage-mid)"/>
        <stop offset="1" stop-color="var(--stage-dark)"/>
      </radialGradient>
      <linearGradient id="hall-tone" x1="0" y1="0" x2="0" y2="1">
        <stop offset="0" stop-color="var(--hall-top)"/>
        <stop offset="0.55" stop-color="var(--hall-mid)"/>
        <stop offset="1" stop-color="var(--hall-bottom)"/>
      </linearGradient>
      <radialGradient id="gold-tone" cx="0.45" cy="0.4" r="0.75">
        <stop offset="0" stop-color="var(--gold-light)"/>
        <stop offset="0.55" stop-color="var(--gold-mid)"/>
        <stop offset="1" stop-color="var(--gold-dark)"/>
      </radialGradient>
    </defs>

    <path class="footer-band" d="M0 812 C140 846 280 872 420 874 C560 852 700 836 812 838 L812 1200 L0 1200 Z" fill="var(--navy)"/>

    <g class="photo-panels" stroke="var(--white)" stroke-width="6" stroke-linejoin="round">
      <path role="img" aria-label="Downtown Los Angeles skyline lit up at night"
            d="M0 140 L390 140 L386 532 C260 542 120 530 0 494 Z" fill="url(#city-tone)"/>
      <path role="img" aria-label="Performer on a concert stage under bright spotlights"
            d="M390 140 L812 140 L812 494 C700 496 560 502 386 524 Z" fill="url(#stage-tone)"/>
      <path role="img" aria-label="Ornate historic theater auditorium with purple lighting"
            d="M0 494 C120 530 260 542 386 532 L414 536 L418 864 C280 860 130 838 0 800 Z" fill="url(#hall-tone)"/>
      <path role="img" aria-label="Gilded historic theater interior with balconies and red stage curtain"
            d="M424 520 C560 504 700 500 812 500 L812 828 C680 828 540 842 424 862 Z" fill="url(#gold-tone)"/>
    </g>

    <path class="header-wave" d="M0 0 L812 0 L812 170 C560 206 300 218 0 150 Z" fill="var(--white)"/>
    <path class="header-rule" d="M0 153 C300 221 560 209 812 173" fill="none" stroke="var(--brand-blue)" stroke-width="7"/>
  </svg>

  <header class="brand">
    <span class="brand-dot"></span>
    <p class="brand-name">
      <span class="line-main">BRIGHTLINE STAGECRAFT</span>
      <span class="line-sub">COMPANY</span>
    </p>
  </header>

  <section class="content">
    <h1 class="headline">Has Open Positions</h1>
    <p class="intro">We are looking for talented technicians<br>to add to our roster of skilled professionals.</p>
    <p class="apply-label">Send Resume to</p>
    <p class="apply-email">APPLY@BSCCREWHUB.LA</p>
    <p class="services">We provide crew for local concerts, filming, theater, and corporate events</p>
  </section>
</main>
</body>
</html>
```